Holistic Psychologist needs contemporary business card

I am a psychologist working with adult clients face to face and online. The card needs to work for clients and also referring doctors and medical professionals. It needs to look warm, safe and trustable for clients, but clean and professional enough for doctors. Sometimes I also work in a corporate context.

I am holistic in my approach (mind-body-spirit) so anything conveying connection or integration or wholeness would be good. But again, clean and contemporary please. It can have a little bit of personality.
New logo uploaded.

Probably warm tones and plenty white space to write on one side.

My web pages:
http://mkcounsel.com.au
https://www.facebook.com/MarionKellerCounselling?ref=hl
Updates

Hi Designers .. I have decided I do need a new logo before finalising a design for the business cards.  I hope to have this available in 4 days from now.

Kindly,

Marion

New logo now posted, same brief.  Balance of masculine and feminine elements, plenty of white space on one side please.

Keen to see some card designs, thank-you.

Target Market(s)

Audience 1 - Males and females aged 25 years + seeking counselling or coaching. Audience 2 - doctors and health professionals who refer clients.

Industry/Entity Type

Medical

Contact Information for Business Card

Logo

Marion Keller
Registered Psychologist

M: 0491 582 034
www.mkcounsel.com.au
marion@mkcounsel.com.au
Little blue Facebook icon, with "marion keller counselling" printed near it.

Font styles to use
Sans Serif

Requirements
Nice to have
• You might want to play with the words "GROUNDED CARE"
Should not have
• Nothing cutesy or too literal

```html
<!DOCTYPE html>
<html lang="en">
<head>
<meta charset="utf-8">
<title>Marion Keller Counselling – Business Card</title>
<link href="https://fonts.googleapis.com/css2?family=Open+Sans:ital,wght@0,400;0,600;0,700;1,400&display=swap" rel="stylesheet">
<style>
  :root {
    --bg: #8a8a8a;
    --card: #ffffff;
    --red: #e3202a;
    --ink: #111111;
    --muted: #333333;
  }
  * { box-sizing: border-box; margin: 0; padding: 0; }
  html, body {
    width: 1200px; height: 900px; overflow: hidden;
    background: var(--bg);
    font-family: "Open Sans", Arial, sans-serif;
  }
  .canvas {
    width: 1200px; height: 900px;
    display: flex; flex-direction: column; align-items: center; justify-content: center;
    gap: 56px;
  }
  .card {
    position: relative;
    width: 600px; height: 366px;
    background: var(--card);
    border-radius: 18px;
    overflow: hidden;
  }

  /* Front */
  .front-lockup {
    position: absolute; left: 0; right: 0; top: 138px;
    display: flex; flex-direction: column; align-items: center;
  }
  .brand-row { display: flex; align-items: center; gap: 12px; }
  .brand-dot {
    width: 26px; height: 26px; border-radius: 50%;
    background: var(--red); flex: none;
  }
  .brand-name {
    color: var(--red); font-weight: 600; font-size: 32px; letter-spacing: 0.5px;
    white-space: nowrap;
  }
  .tagline {
    margin-top: 10px; margin-left: 38px;
    color: var(--red); font-weight: 700; font-size: 15px; letter-spacing: 0.5px;
  }

  /* Back */
  .back-brand {
    position: absolute; right: 30px; top: 32px;
    display: flex; align-items: center; gap: 10px;
  }
  .back-brand .brand-dot { width: 20px; height: 20px; }
  .back-brand .brand-name { font-size: 24px; }

  .tab-black { position: absolute; left: 0; top: 118px; width: 16px; height: 42px; background: var(--ink); }
  .tab-red   { position: absolute; left: 0; top: 160px; width: 16px; height: 92px; background: var(--red); }
  .edge-red  { position: absolute; right: 0; top: 226px; width: 16px; height: 76px; background: var(--red); }

  .person { position: absolute; left: 46px; top: 120px; }
  .person-name { font-weight: 700; font-size: 20px; color: var(--ink); }
  .person-role { font-size: 12px; color: var(--muted); margin-top: 1px; }

  .contacts { position: absolute; left: 40px; top: 188px; list-style: none; }
  .contacts li {
    display: flex; align-items: center; gap: 10px;
    font-size: 13.5px; color: var(--ink); line-height: 20px;
  }
  .icon {
    width: 14px; height: 14px; border-radius: 2px; background: var(--red);
    display: flex; align-items: center; justify-content: center; flex: none;
  }
  .icon svg { width: 10px; height: 10px; }
</style>
</head>
<body>
<main class="canvas">

  <section class="card card-front" aria-label="Card front">
    <div class="front-lockup">
      <div class="brand-row">
        <span class="brand-dot"></span>
        <span class="brand-name">Marion Keller Counselling</span>
      </div>
      <div class="tagline">GROUNDED CARE</div>
    </div>
  </section>

  <section class="card card-back" aria-label="Card back">
    <div class="back-brand">
      <span class="brand-dot"></span>
      <span class="brand-name">Marion Keller Counselling</span>
    </div>

    <span class="tab-black"></span>
    <span class="tab-red"></span>
    <span class="edge-red"></span>

    <div class="person">
      <div class="person-name">Marion Keller</div>
      <div class="person-role">Registered Psychologist</div>
    </div>

    <ul class="contacts">
      <li>
        <span class="icon"><svg viewBox="0 0 10 10"><rect x="2.5" y="0.5" width="5" height="9" rx="1" fill="#fff"/><rect x="3.5" y="1.8" width="3" height="5.5" fill="#e3202a"/></svg></span>
        0491 582 034
      </li>
      <li>
        <span class="icon"><svg viewBox="0 0 10 10"><rect x="0.5" y="2" width="9" height="6" fill="#fff"/><path d="M0.5 2 L5 5.5 L9.5 2" stroke="#e3202a" stroke-width="1" fill="none"/></svg></span>
        marion@mkcounsel.com.au
      </li>
      <li>
        <span class="icon"><svg viewBox="0 0 10 10" fill="none" stroke="#fff" stroke-width="1"><circle cx="5" cy="5" r="4"/><ellipse cx="5" cy="5" rx="1.8" ry="4"/><path d="M1 5 H9"/></svg></span>
        www.mkcounsel.com.au
      </li>
      <li>
        <span class="icon"></span>
        /MarionKellerCounselling
      </li>
    </ul>
  </section>

</main>
</body>
</html>
```